Web Design Project - Event Management Company

A web-page design needs to be created for an event management company. The logo has already been created, the design needs to draw on the themes and colors of the logo and extend on that.

The event management company likes to differentiate itself from others by being a bit "un-conventional" and being able to think outside the box.

the specialise in corporate events, weddings, AGMs, anything that requires coordination of resources. They also can provide Audio Visual services such as recording events.

final design will also require HTML implementation

```html
<!DOCTYPE html>
<html lang="en">
<head>
<meta charset="utf-8">
<title>Odd Block Events</title>
<link href="https://fonts.googleapis.com/css2?family=Ubuntu:wght@400;500;700&display=swap" rel="stylesheet">
<style>
:root{
  --page:#ececec;
  --panel:#f7f7f7;
  --panel-line:#dcdcdc;
  --ink:#2b2b2b;
  --muted:#666;
  --magenta:#a3127f;
  --pink:#e6267a;
  --yellow:#e8b82a;
  --dark:#1c1c1c;
  --tile:#2e2e2e;
  --nav:#3d3f44;
  --fb-blue:#3b5998;
}
*{box-sizing:border-box;margin:0;padding:0}
html,body{width:905px;height:1200px;overflow:hidden}
body{position:relative;background:var(--page);font-family:"Ubuntu",sans-serif;color:var(--ink);font-size:9px;line-height:1.35}
.abs{position:absolute}
a{color:inherit;text-decoration:none}

.masthead{left:0;top:0;width:905px;height:118px;
  background:
   radial-gradient(ellipse 260px 120px at 420px 10px,rgba(214,190,40,.95),rgba(214,190,40,0) 70%),
   radial-gradient(ellipse 300px 140px at 250px 60px,rgba(190,20,110,.85),rgba(190,20,110,0) 75%),
   linear-gradient(90deg,#3a0722 0%,#7d1150 25%,#9a5a35 45%,#9b8e2a 58%,#3d5a3c 78%,#0f1a1e 100%);}
.brand{left:157px;top:0;width:122px;height:66px;background:#fff;border-radius:0 0 7px 7px;box-shadow:0 1px 3px rgba(0,0,0,.4);display:flex;flex-direction:column;align-items:center;justify-content:center;gap:6px}
.brand-mark{width:22px;height:22px;background:var(--pink)}
.brand-name{font-size:11px;font-weight:500;color:#333;letter-spacing:.2px}
.utility{right:134px;top:18px;color:#fff;font-size:8px}
.utility span{margin:0 4px;opacity:.8}
.search{left:618px;top:46px;width:153px;height:20px;display:flex}
.search-field{flex:1;background:#fff;border:1px solid #bbb;font-size:8.5px;padding:4px 6px;color:#333}
.search-btn{width:20px;background:#222;display:flex;align-items:center;justify-content:center}

.nav{left:134px;top:86px;width:638px;height:32px;display:flex;background:var(--nav)}
.nav-home{width:47px;background:#dedede;display:flex;align-items:center;justify-content:center}
.nav a{flex:1;color:#fff;font-size:11.5px;display:flex;align-items:center;justify-content:center;border-left:1px solid #4e5156}

.panel{background:var(--panel);border:1px solid var(--panel-line)}
.panel-title{font-size:15.5px;font-weight:400;color:#222;letter-spacing:.2px}
.view-all{font-size:8.5px;color:var(--magenta)}

.hero{left:134px;top:126px;width:423px;height:266px}
.hero-stage{left:8px;top:7px;width:408px;height:253px;background:#111}
.hero-photo{left:0;top:0;width:408px;height:173px;background:linear-gradient(160deg,#7a77c9 0%,#a35bb0 40%,#5c2c6a 75%,#2a1430 100%)}
.hero-caption{left:0;top:164px;width:408px;height:36px;background:rgba(0,0,0,.45);color:#fff;font-size:15px;padding:9px 7px}
.thumb{top:201px;width:93px;height:43px}
.thumb.active{outline:3px solid #fff;outline-offset:-3px}

.promo{left:564px;width:208px;height:88px;background:var(--dark)}
.promo-photo{left:0;top:0;width:102px;height:87px}
.promo-text{left:111px;top:0;height:88px;display:flex;flex-direction:column;justify-content:center;color:#fff;font-size:9.5px;line-height:1.15}
.promo-big{font-size:15px}

.events{left:134px;top:398px;width:423px;height:254px}
.event-list{left:14px;top:34px;width:396px;height:208px;background:#fff;border:1px solid #e2e2e2}
.event{display:flex;height:52px;padding:7px 6px;border-bottom:1px solid #e8e8e8}
.event:last-child{border-bottom:0}
.avatar{width:43px;height:38px;flex:none;margin-right:8px}
.date{color:var(--magenta);font-size:9px;margin-bottom:1px}
.event p{font-size:8.6px;color:#333}

.video-title{left:564px;top:398px;width:208px;border-bottom:1px solid #cfcfcf;padding-bottom:3px}
.video{left:564px;top:426px;width:208px;height:171px;background:#000}
.video-frame{left:0;top:0;width:208px;height:155px;background:radial-gradient(ellipse at 50% 30%,#c3a0e0 0%,#6a3ea0 35%,#2a1840 70%,#0c0814 100%)}
.video-bar{left:0;top:155px;width:208px;height:16px;background:#1a1a1a}
.progress{left:0;top:157px;width:208px;height:2px;background:#555}
.progress-fill{left:0;top:157px;width:89px;height:2px;background:#d11}
.progress-knob{left:86px;top:155px;width:6px;height:6px;border-radius:50%;background:#eee}
.time{left:29px;top:162px;color:#bbb;font-size:5px}

.follow{left:564px;top:608px;width:208px;height:77px}
.social{top:36px;width:28px;height:28px;border-radius:4px}

.fb{left:564px;top:693px;width:208px;height:171px;background:#fff}
.fb-head{left:13px;top:8px;display:flex;gap:7px}
.fb-sq{width:24px;height:24px;background:var(--fb-blue)}
.fb-name{color:var(--fb-blue);font-weight:700;font-size:9px}
.fb-like{margin-top:4px;border:1px solid #c5cbd9;background:#eceef5;color:#3b5998;font-size:7px;padding:1px 4px;display:inline-block}
.fb-count{left:13px;top:43px;font-size:7px;color:#333}
.fb-grid{left:13px;top:55px;width:185px;display:grid;grid-template-columns:repeat(5,33px);column-gap:4px;row-gap:4px}
.fb-face{width:33px;height:33px}
.fb-label{font-size:6px;color:#666;text-align:center;margin-top:1px}
.fb-foot{left:13px;top:158px;font-size:6.5px;color:var(--fb-blue);display:flex;gap:4px;align-items:center}
.fb-foot i{width:8px;height:8px;background:var(--fb-blue);display:block}

.stars{left:134px;top:660px;width:423px;height:202px}
.star-grid{left:14px;top:33px;width:398px;height:156px;display:grid;grid-template-columns:1fr 1fr;background:var(--tile)}
.star{display:flex;padding:6px 6px;height:52px;border-right:1px solid #222;border-bottom:1px solid #222}
.star:nth-child(4n+2),.star:nth-child(4n+3){background:#353535}
.star .avatar{width:43px;height:38px;margin-right:9px}
.star .date{color:#aaa}
.star p{color:#fff;font-size:8.6px}

.about{left:134px;top:870px;width:423px;height:256px;padding:12px 13px}
.about p{font-size:8.6px;color:#333;margin-top:9px;line-height:1.38}
.about .panel-title{margin-bottom:-2px}
.about .view-all{position:absolute;right:14px;bottom:13px}

.reviews{left:564px;top:870px;width:208px;height:256px;padding:12px 13px}
.review{padding:8px 0 9px;border-bottom:1px solid #e0e0e0}
.review:last-of-type{border-bottom:0}
.review h4{color:var(--magenta);font-weight:400;font-size:8.8px;margin-bottom:2px}
.review p{font-size:8.6px;color:#333}
.reviews .view-all{position:absolute;right:14px;bottom:13px}

.footer-links{left:134px;top:1146px;font-size:7.5px;color:#666}
.footer-links b{color:#222;font-weight:400}
.footer-links span{margin:0 4px}
.copyright{left:134px;top:1164px;font-size:7.5px;color:#666}
</style>
</head>
<body>

<header class="abs masthead"></header>
<div class="abs brand"><div class="brand-mark"></div><div class="brand-name">ODD BLOCK EVENTS</div></div>
<div class="abs utility"><a>Sign In</a><span>|</span><a>Register</a><span>|</span><a>Site Map</a><span>|</span><a>FAQs</a></div>
<div class="abs search">
  <div class="search-field">SEARCH</div>
  <div class="search-btn"><svg width="11" height="11" viewBox="0 0 11 11"><circle cx="4.5" cy="4.5" r="3.3" fill="none" stroke="#fff" stroke-width="1.6"/><line x1="7" y1="7" x2="10" y2="10" stroke="#fff" stroke-width="1.8"/></svg></div>
</div>
<nav class="abs nav">
  <div class="nav-home"><svg width="14" height="12" viewBox="0 0 14 12"><path d="M7 0L0 6h2v6h4V8h2v4h4V6h2z" fill="#777"/></svg></div>
  <a>EVENTS</a><a>REVIEWS</a><a>INTERVIEWS</a><a>COMPETITIONS</a><a>NEWS</a><a>CONTACTS</a>
</nav>

<section class="abs panel hero">
  <div class="abs hero-stage">
    <div class="abs hero-photo" role="img" aria-label="Band performing on stage under purple lights"></div>
    <div class="abs hero-caption">Aliquam at erat sed nunc consequat molestie</div>
    <div class="abs thumb active" style="left:7px;background:linear-gradient(135deg,#8f88d0,#a050a8)" role="img" aria-label="Band thumbnail"></div>
    <div class="abs thumb" style="left:107px;background:linear-gradient(135deg,#3a3a10,#c8b030)" role="img" aria-label="Concert stage thumbnail"></div>
    <div class="abs thumb" style="left:207px;background:linear-gradient(135deg,#1a2a80,#6a70d0)" role="img" aria-label="Singer thumbnail"></div>
    <div class="abs thumb" style="left:307px;background:linear-gradient(135deg,#5a4a3a,#b0a090)" role="img" aria-label="Group photo thumbnail"></div>
  </div>
</section>

<div class="abs promo" style="top:126px">
  <div class="abs promo-photo" style="background:linear-gradient(180deg,#9aa4a8,#3a4246)" role="img" aria-label="Band group photo"></div>
  <div class="abs promo-text"><span>VOTE FOR</span><span class="promo-big" style="color:var(--yellow)">ODD BLOCK<br>EVENTS</span></div>
</div>
<div class="abs promo" style="top:215px">
  <div class="abs promo-photo" style="background:linear-gradient(135deg,#556070,#c8c8c0)" role="img" aria-label="Musician at an event"></div>
  <div class="abs promo-text"><span class="promo-big" style="color:var(--pink)">PICTURE</span><span>OF THE WEEK</span></div>
</div>
<div class="abs promo" style="top:304px">
  <div class="abs promo-photo" style="background:linear-gradient(135deg,#7a1010,#2a2a70 60%,#4a1a8a)" role="img" aria-label="Collage of performing artists"></div>
  <div class="abs promo-text"><span class="promo-big" style="color:var(--magenta)">2011<br>ARTISTS</span><span>TO WATCH</span></div>
</div>

<section class="abs panel events">
  <h2 class="abs panel-title" style="left:14px;top:9px">LATEST EVENTS</h2>
  <a class="abs view-all" style="right:14px;top:13px">view all »</a>
  <div class="abs event-list">
    <div class="event"><div class="avatar" style="background:#3a3026" role="img" aria-label="Artist portrait"></div><div><div class="date">Wednesday, 31 July, 2013</div><p>Donec bibendum lacinia rutrum. Aliquam at erat sed nunc consequat moles-<br>tie. Maecenas arcu quam, facilisis et gravida vel..</p></div></div>
    <div class="event"><div class="avatar" style="background:#555" role="img" aria-label="Artist portrait"></div><div><div class="date">Wednesday, 31 July, 2013</div><p>Donec bibendum lacinia rutrum. Aliquam at erat sed nunc consequat moles-<br>tie. Maecenas arcu quam...</p></div></div>
    <div class="event"><div class="avatar" style="background:#4a4a3a" role="img" aria-label="Artist portrait"></div><div><div class="date">Wednesday, 31 July, 2013</div><p>Donec bibendum lacinia rutrum. Aliquam at erat sed nunc consequat moles-<br>tie. Maecenas arcu quam, facilisis et gravida vel..</p></div></div>
    <div class="event"><div class="avatar" style="background:#b06030" role="img" aria-label="Artist portrait"></div><div><div class="date">Wednesday, 31 July, 2013</div><p>Donec bibendum lacinia rutrum. Aliquam at erat sed nunc consequat moles-<br>tie. Maecenas arcu quam, facilisis et gravida..</p></div></div>
  </div>
</section>

<h2 class="abs panel-title video-title">LATEST VIDEO</h2>
<div class="abs video">
  <div class="abs video-frame" role="img" aria-label="Crowd at a concert under stage lights"></div>
  <div class="abs video-bar"></div>
  <div class="abs progress"></div>
  <div class="abs progress-fill"></div>
  <div class="abs progress-knob"></div>
  <svg class="abs" style="left:7px;top:162px" width="16" height="6" viewBox="0 0 16 6"><path d="M0 0l5 3-5 3z" fill="#aaa"/><rect x="10" y="1" width="3" height="4" fill="#aaa"/></svg>
  <div class="abs time">1:14 / 2:56</div>
  <svg class="abs" style="left:160px;top:162px" width="44" height="6" viewBox="0 0 44 6"><circle cx="3" cy="3" r="2.3" fill="#888"/><circle cx="13" cy="3" r="2.3" fill="#888"/><rect x="21" y="0.5" width="7" height="5" fill="none" stroke="#aaa"/><rect x="32" y="0.5" width="5" height="5" fill="none" stroke="#aaa"/><rect x="39" y="0.5" width="5" height="5" fill="none" stroke="#888"/></svg>
</div>

<section class="abs panel follow">
  <h2 class="abs panel-title" style="left:13px;top:9px">FOLLOW US ON</h2>
  <div class="abs social" style="left:14px;background:#2d5aa8"></div>
  <div class="abs social" style="left:54px;background:#3aa0d8"></div>
  <div class="abs social" style="left:93px;background:#1f6fb8"></div>
  <div class="abs social" style="left:132px;background:#f08a1a"></div>
</section>

<section class="abs panel fb">
  <div class="abs fb-head"><div class="fb-sq"></div><div><div class="fb-name">Crowdsphere Platform</div><span class="fb-like">Like</span></div></div>
  <div class="abs fb-count">3,621,040 people like <b>Crowdsphere Platform</b>.</div>
  <div class="abs fb-grid">
    <div><div class="fb-face" style="background:#8a7a60" role="img" aria-label="Member photo"></div><div class="fb-label">Marco</div></div>
    <div><div class="fb-face" style="background:#6a5a50" role="img" aria-label="Member photo"></div><div class="fb-label">Lena</div></div>
    <div><div class="fb-face" style="background:#bbb" role="img" aria-label="Member photo"></div><div class="fb-label">Ravi</div></div>
    <div><div class="fb-face" style="background:#7a5030" role="img" aria-label="Member photo"></div><div class="fb-label">Tessa</div></div>
    <div><div class="fb-face" style="background:#5a4a4a" role="img" aria-label="Member photo"></div><div class="fb-label">Dorian</div></div>
    <div><div class="fb-face" style="background:#a08060" role="img" aria-label="Member photo"></div><div class="fb-label">Lara</div></div>
    <div><div class="fb-face" style="background:#8aa0c0" role="img" aria-label="Member photo"></div><div class="fb-label">Pavel</div></div>
    <div><div class="fb-face" style="background:#d8c070" role="img" aria-label="Member photo"></div><div class="fb-label">Bruno</div></div>
    <div><div class="fb-face" style="background:#606060" role="img" aria-label="Member photo"></div><div class="fb-label">Samir</div></div>
    <div><div class="fb-face" style="background:#9a9a9a" role="img" aria-label="Member photo"></div><div class="fb-label">Ines</div></div>
  </div>
  <div class="abs fb-foot"><i></i>Crowdsphere social plugin</div>
</section>

<section class="abs panel stars">
  <h2 class="abs panel-title" style="left:14px;top:8px">TOP STAR NEWS</h2>
  <a class="abs view-all" style="right:14px;top:12px">view all »</a>
  <div class="abs star-grid">
    <div class="star"><div class="avatar" style="background:#7a4a3a" role="img" aria-label="Star portrait"></div><div><div class="date">Wednesday, 31 July, 2013</div><p>Donec bibendum lacinia<br>rutrum. Aliquam at erat sed</p></div></div>
    <div class="star"><div class="avatar" style="background:#8a3030" role="img" aria-label="Star portrait"></div><div><div class="date">Wednesday, 31 July, 2013</div><p>Donec bibendum lacinia<br>rutrum. Aliquam at erat sed</p></div></div>
    <div class="star"><div class="avatar" style="background:#6a4020" role="img" aria-label="Star portrait"></div><div><div class="date">Wednesday, 31 July, 2013</div><p>Donec bibendum lacinia<br>rutrum. Aliquam at erat sed</p></div></div>
    <div class="star"><div class="avatar" style="background:#d8d040" role="img" aria-label="Star portrait"></div><div><div class="date">Wednesday, 31 July, 2013</div><p>Donec bibendum lacinia<br>rutrum. Aliquam at erat sed</p></div></div>
    <div class="star"><div class="avatar" style="background:#b02a1a" role="img" aria-label="Star portrait"></div><div><div class="date">Wednesday, 31 July, 2013</div><p>Donec bibendum lacinia<br>rutrum. Aliquam at erat sed</p></div></div>
    <div class="star"><div class="avatar" style="background:#6a5048" role="img" aria-label="Star portrait"></div><div><div class="date">Wednesday, 31 July, 2013</div><p>Donec bibendum lacinia<br>rutrum. Aliquam at erat sed</p></div></div>
  </div>
</section>

<section class="abs panel about">
  <h2 class="panel-title">ABOUT US</h2>
  <p>Lorem ipsum dolor sit amet, consectetur adipiscing elit. Nulla lobortis justo a arcu molestie iaculis. Aenean volutpat condimentum elementum. Mauris vel felis vitae lorem malesuada aliquam. Aenean egestas pellentesque sapien, ac tristique velit aliquet ut. Integer id erat justo. Nam vel est orci. Curabitur in leo lorem. Donec in augue a magna tristique tristique eget a metus. Ut elit sapien, semper eu aliquam in, porta sit amet purus. Vestibulum gravida lorem nec urna tincidunt eget tincidunt augue varius.</p>
  <p>Vivamus at arcu ut magna blandit vulputate ac vel mauris. Morbi eget tortor metus. Aenean nec interdum neque. Pellentesque habitant morbi tristique senectus et netus et malesuada fames ac turpis egestas.</p>
  <p>Nulla adipiscing metus eget nulla tincidunt et tincidunt dolor euismod. Integer bibendum, enim non tincidunt congue, magna mi pellentesque diam, auctor tristique urna sem nec est. Curabitur sed dapibus metus. Vestibulum ut leo ac massa vestibulum gravida vitae id velit. Maecenas est orci, semper sed ullamcorper quis, pellentesque ut nibh.</p>
  <a class="view-all">read more »</a>
</section>

<section class="abs panel reviews">
  <h2 class="panel-title">RECENT REVIEWS</h2>
  <div class="review"><h4>Lorem ipsum dolor sit amet</h4><p>Consectetur adipiscing elit. Nulla lobortis justo a arcu molestie iaculis. Aenean vol utpat condimentum elementum.</p></div>
  <div class="review"><h4>Lorem ipsum dolor sit amet</h4><p>Consectetur adipiscing elit. Nulla lobortis justo a arcu molestie iaculis. Aenean vol utpat condimentum elementum.</p></div>
  <div class="review"><h4>Lorem ipsum dolor sit amet</h4><p>Consectetur adipiscing elit. Nulla lobortis justo a arcu molestie iaculis. Aenean vol utpat condimentum.</p></div>
  <a class="view-all">view all »</a>
</section>

<footer>
  <div class="abs footer-links"><b>Home</b><span>|</span>Events<span>|</span>Reviews<span>|</span>Interviews<span>|</span>Competitions<span>|</span>News<span>|</span>Contacts</div>
  <div class="abs copyright">Copyright © 2013 Odd Block Events | Privacy Policy</div>
</footer>

</body>
</html>
```